banner for website

I need a new banner for my website. My website now is. www.brightmeadowkitchenway.com, but I'm changing it to Verdant Daily Table and I need a new banner. I want me to be who it's about. I am my brand. I'm Marla Pennick. So, my name needs to be prominent in the banner along with my photo, which I'm attaching. I want my photo very prominent in the banner and very large. I am attaching my two favorites.
I need the banner plain ( with out the newsletter sign up optin part), so I can use it on my newsletters, emails and letter head, as well. I would like it to be inviting. I I have a certain color scheme I use. Deep dark brown letters with blues and greens. Very earthy and psychologically grounded. I would like to keep that color scheme. In my website banner, I need a opt in to sign up for my free monthly newsletter and receive my Free Pantry Basket Planner.

I want the shopping guide to be small and pleasant looking and to say: "Sign up to receive your Free Pantry Basket Planner and monthly newsletter."

I only want my banner to say: "Verdant Daily Table" "Marla Pennick"

I would also like to have part of the banner without the sign in for the newsletter part off of it. And also one with only the "Verdant Daily Table" and one with "Verdant Daily Table" and "Marla Pennick" without the newsletter sign up part on it either.

I hope you can do this for me. I look forward to seeing your design! Sincerely, Marla
Updates

Project Deadline Extended Reason: I couldn't view the designs so I couldn't look at the ones submitted. I just now got into the website with your company's help. I don't want to be penalized because of a problem with the log in at your site. That was not my fault. Please let me know your thoughts. Added Monday, May 9, 2016

Target Market(s)

people over 40 who have bad health or who want to learn how to be a vegetarian for better health.

Number of Pages Required

1 page

Requirements
Must have
• I want the shopping guide to be small and pleasant looking and to say: "Sign up to receive your Free Pantry Basket Planner and monthly newsletter." I would like it to blend and be elegant and not in the middle of the banner or across my face.
• I only want my banner to say: "Verdant Daily Table" "Marla Pennick"
• I would also like to have part of the banner without the sign in for the newsletter part off of it. And also one with only the "Verdant Daily Table" and one with "Verdant Daily Table" and "Marla Pennick" without the newsletter sign up part on it either.
Nice to have
• Nice font and colors. I want the background to be plants and earthy and inviting.
Should not have
• I updated and added two new photos. I think the one you were using with me in the red top looked funny under my eyes. it was too pink or something. I uploaded a better version of that photo. in hopes that it looks better. Please switch those out if you are using the one with me in the red top.

```html
<!DOCTYPE html>
<html lang="en">
<head>
<meta charset="utf-8">
<title>Verdant Daily Table — Marla Pennick</title>
<link href="https://fonts.googleapis.com/css2?family=Noto+Serif:ital,wght@0,400;0,700;1,400&family=Open+Sans:wght@400;600&display=swap" rel="stylesheet">
<style>
  :root {
    --nav-brown: #43382b;
    --nav-text: #f4efe6;
    --accent-orange: #e0702a;
    --leaf-green: #3f7d1f;
    --link-green: #3f6b2a;
    --heading-ink: #4b4b4b;
    --body-ink: #5a5a5a;
    --brand-blue: #1d63c9;
    --rule-grey: #dcdcdc;
    --page-white: #ffffff;
  }
  * { box-sizing: border-box; margin: 0; padding: 0; }
  html, body { width: 1200px; height: 1041px; overflow: hidden; background: var(--page-white); }
  body { font-family: "Open Sans", sans-serif; color: var(--body-ink); position: relative; }

  /* Header banner */
  .banner {
    position: absolute; left: 0; top: 0; width: 1200px; height: 380px;
    background: linear-gradient(100deg, #5b5d52 0%, #8a8b7d 30%, #b9bcae 55%, #d6d8cc 75%, #9fa88c 100%);
    overflow: hidden;
  }
  .banner-portrait {
    position: absolute; left: 680px; top: 0; width: 430px; height: 392px;
    background: radial-gradient(ellipse at 55% 40%, #e9c9a8 0%, #c98a5e 28%, #a2362a 52%, #5f7f3a 75%, rgba(95,127,58,0) 100%);
  }
  .brand-name {
    position: absolute; left: 163px; top: 80px;
    font-family: "Noto Serif", serif; font-weight: 700; font-size: 40px;
    color: var(--brand-blue); white-space: nowrap;
  }
  .person-name {
    position: absolute; left: 160px; width: 420px; top: 224px; text-align: center;
    font-family: "Open Sans", sans-serif; font-weight: 600; font-size: 36px;
    letter-spacing: 3px; color: #f2f2f2; text-shadow: 0 2px 4px rgba(0,0,0,.6);
  }
  .optin {
    position: absolute; left: 160px; width: 420px; top: 307px; text-align: center;
    border-top: 1px solid rgba(255,255,255,.5); border-bottom: 1px solid rgba(255,255,255,.7);
    padding: 4px 0 6px; font-size: 15px; line-height: 18px; color: #fff;
    text-shadow: 0 1px 2px rgba(0,0,0,.6);
  }

  /* Navigation */
  .main-nav {
    position: absolute; left: 0; top: 380px; width: 1200px; height: 50px;
    background: var(--nav-brown); box-shadow: 0 3px 5px rgba(0,0,0,.25);
  }
  .main-nav ul { list-style: none; display: flex; position: absolute; left: 144px; top: 4px; }
  .main-nav li {
    font-family: "Noto Serif", serif; font-weight: 700; font-size: 13.5px;
    color: var(--nav-text); padding: 0 12px; height: 46px; line-height: 36px;
  }
  .main-nav li.is-active { background: var(--page-white); color: var(--accent-orange); font-weight: 400; }

  /* Features */
  .features { position: absolute; left: 0; top: 430px; width: 1200px; height: 256px; }
  .feature { position: absolute; top: 40px; width: 300px; }
  .feature-thumb { position: absolute; left: 0; top: 0; width: 95px; height: 95px; }
  .feature-body { position: absolute; left: 119px; top: 0; width: 180px; }
  .feature h2 {
    font-family: "Noto Serif", serif; font-weight: 400; font-size: 21px; line-height: 22px;
    color: var(--heading-ink); margin-bottom: 14px;
  }
  .feature p { font-size: 12.5px; line-height: 19px; color: var(--body-ink); }
  .learn-more {
    display: block; margin-top: 9px; font-family: "Noto Serif", serif; font-style: italic;
    font-size: 14px; color: var(--link-green); text-decoration: none;
  }

  .divider {
    position: absolute; left: 0; top: 686px; width: 1200px; height: 26px;
    border-top: 3px solid #4a4a46;
    background: linear-gradient(#e4e4e4, #ffffff);
  }

  /* Content */
  .content { position: absolute; left: 178px; top: 712px; width: 560px; }
  .content h1 {
    font-family: "Noto Serif", serif; font-weight: 400; font-size: 37px; color: var(--leaf-green);
    margin-top: 6px; margin-bottom: 16px;
  }
  .book-cover { float: left; width: 119px; height: 174px; margin: 0 10px 4px 0; background: linear-gradient(#d7d2cb, #5a3b3f 70%, #8a3a2c); }
  .book-title { font-weight: 600; font-size: 14px; color: #4a4a4a; line-height: 24px; }
  .content p { font-size: 14px; line-height: 24px; color: var(--body-ink); }
  .content p + p { margin-top: 10px; }

  /* Sidebar */
  .sidebar { position: absolute; left: 790px; top: 720px; width: 257px; }
  .sidebar h3 {
    font-family: "Noto Serif", serif; font-weight: 400; font-size: 16px; color: var(--heading-ink);
    padding-bottom: 10px; border-bottom: 3px double var(--rule-grey);
  }
  .social-row { display: flex; gap: 13px; margin: 14px 0 8px 4px; }
  .social-row span { width: 28px; height: 28px; border-radius: 5px; background: #7f9bb0; }
  .event-ad { width: 228px; height: 158px; margin: 38px 0 0 15px; background: linear-gradient(120deg, #6fb7c9, #b8d9c0 55%, #efe2c9); }
</style>
</head>
<body>
  <header class="banner">
    <div class="banner-portrait" role="img" aria-label="Marla Pennick smiling, holding a basket of fresh vegetables beside a large white daisy"></div>
    <div class="brand-name">Verdant Daily Table</div>
    <div class="person-name">MARLA PENNICK</div>
    <div class="optin">Sign up to receive your free pantry basket planner and monthly newsletter</div>
  </header>

  <nav class="main-nav">
    <ul>
      <li class="is-active">Home</li>
      <li>Speaking »</li>
      <li>Counseling »</li>
      <li>Retreats &amp; Classes</li>
      <li>Meet Marla »</li>
      <li>Store »</li>
      <li>Blog</li>
      <li>References</li>
      <li>Media</li>
    </ul>
  </nav>

  <section class="features">
    <article class="feature" style="left:154px">
      <div class="feature-thumb" role="img" aria-label="Marla speaking on stage" style="background:linear-gradient(#c9c8c6,#7d7a76)"></div>
      <div class="feature-body">
        <h2>Motivational Speaker</h2>
        <p>Marla is a member of the Guild of Keynote Presenters, traveling internationally, employee wellness programs and ...</p>
        <a class="learn-more">Learn more</a>
      </div>
    </article>
    <article class="feature" style="left:458px">
      <div class="feature-thumb" role="img" aria-label="Framed portrait of Marla with a microphone" style="background:linear-gradient(135deg,#e7d6d8,#a89a9c)"></div>
      <div class="feature-body">
        <h2>Nutrition Counseling</h2>
        <p>Whether you are looking for individualized personal health &amp; nutrition counseling, family coaching, cooking classes or a private...</p>
        <a class="learn-more">Learn more</a>
      </div>
    </article>
    <article class="feature" style="left:762px">
      <div class="feature-thumb" role="img" aria-label="Stack of Marla's cookbooks and DVDs" style="background:linear-gradient(135deg,#3f5a2e,#c9c2a8 60%,#8a5a2c)"></div>
      <div class="feature-body">
        <h2>Best Nutrition, Books &amp; Products</h2>
        <p>Books &amp; DVD's on nutrition &amp; healthy recipes. Food, Body Care, &amp; Home Products. Find it all here.</p>
        <a class="learn-more">Learn more</a>
      </div>
    </article>
  </section>

  <div class="divider"></div>

  <main class="content">
    <h1>Best Nutrition Books</h1>
    <div class="book-cover" role="img" aria-label="Book cover: a baby in a chef's hat with vegetables"></div>
    <div class="book-title">Growing Bright Eaters</div>
    <p>Finally! A Comprehensive Guide to Raising Healthy Kids in Today's World! "Growing Bright Eaters" gives a parent the power of healthy choices. A comprehensive guidebook to create long-term, sustainable, and life-enhancing strategies for raising healthier children through nutrition. In this book, #1 bestselling Author Marla Pennick inspires, motivates, and teaches easy-to-implement suggestions as well as offers incredible insight into health and wellness for kids of all ages, recipes included! Healthy foods &amp; healthy life!</p>
    <p>“Marla Pennick’s book is a comprehensive guidebook to create long-term sustainable and life-enhancing strategies through nutrition. In this book, she inspires, motivates and teaches</p>
  </main>

  <aside class="sidebar">
    <h3>Follow Marla Pennick</h3>
    <div class="social-row"><span></span><span></span><span></span><span></span><span></span></div>
    <h3>Get Marla for Your Event</h3>
    <div class="event-ad" role="img" aria-label="Promotion to book Marla for your next speaking engagement, with her photo and a microphone"></div>
  </aside>
</body>
</html>
```